Brochure for Training & Coaching Company
Design a single page double sided brochure that mirrors excisting website
Brochure for Training & Coaching Company - Education
Creative Brief
Education
Could be companies, could be private persons.
Needs to be delivered in an editable Photoshop or Illustrator file. Brochure will probably be used to create a newsletter as well using for example Mailchimp.
Reinout Reinout
If the text is too long, I could reduce it a bit, like: ---- [title-->]Retraite: Leiding geven aan jezelf. [subtitle-->]5 daags programma [targetting-->]Herken je dit: je bent een harde werker maar je hebt contact verloren met wat je nu echt wilt van het leven. Je leven zitten vol “moeten” en je loopt op je tenen om anderen te pleasen. Je bent bewust dat je vanuit je hoofd leeft en je graag in contact wilt komen met wat je passie en je drijfveren zijn. Je wilt graag naar een andere manier van leidinggeven? Meer betrokken zijn en faciliteren..invloed hebben op je medewerkers? Je taak zien als inspirerend, motiverend? Meer voldoening en minder stress? Met zin naar je werk gaan omdat je bijdrage zingevend is! [programme-->]Leiderschap: de kracht succesvol en authentiek te zijn Wij geloven dat elke verandering begint in jezelf met kennis van jezelf. Bewustwording van wie jij bent als leidinggevende, manager, directeur of zzp-er is de eerste stap naar geluk, vrijheid en succes. En dat is precies waar we jou mee helpen. Zakelijk succes en inspirerend leiderschap hangen nauw samen met jouw persoonlijke ontwikkeling. En persoonlijke ontwikkeling is een noodzaak voor de groei van elk individu en iedere onderneming. Werken vanuit het “Nu” In deze retraite laten we het programma op een organische wijze ontstaan, samen geven we inhoud. Geen controle maar de dynamische processen in jezelf en de groep laten gebeuren geeft een enorme kracht en werkt energie verhogend. We werken vanuit 3 verschillende stappen: Bewustwording: Je zelfbeeld, overtuigingen en patronen, en vanuit welke potentie geef je nu leiding, creativiteit verhogen, Leren creëren Empowerment: het ontwikkelen van eigen kracht, potentie, talenten en mogelijkheden. In contact komen met je drijfveren, Verhogen van je bewustzijn, Toekomstperspectief: een concreet plan maken, Je verlangen volgen, Van beperking naar overvloed, Laat je inspireren door de Renaissance Naast de nodige diepgang, biedt het programma ook ruimte. Zo bezoeken Urbino en laten we ons inspireren door het verhaal van Duca Ottavio di Rocchalta. Daarnaast maken we heerlijke wandelingen te maken door het heuvellandschap, waarbij er voldoende tijd is om na te denken en met elkaar contact te maken en intervisie gesprekken te voeren. [results-->]Resultaten die je mag verwachten - Je bent meer zelfbewust, weet wat belangrijk voor je is, dat is de basis van persoonlijk leiderschap. - Je hebt kennis en inzicht in jouw drijfveren en bronnen ter inspiratie aan je persoonlijke ontwikkeling en leiderschap. - Je geeft actief invulling aan je verschillende rollen op de manier die je past en weet daarmee mensen mee te krijgen en te inspireren. Voorbereiding en nazorg Na je aanmelding krijg je een telefonisch kennismakingsgesprek en een inschrijfformulier. Dat betekent dat we ons samen goed kunnen voorbereiden op de aandachtspunten. Voor wie Deze reis is geschikt voor leidinggevenden, managers, directeuren of zzp-ers van alle leeftijden. [prize-->]Prijzen Inclusief is: - Vervoer van vliegveld Bologna, Italië tot aan het Resort en weer terug - Eenpersoonskamer op het Resort, all inclusive Exclusief is: - Vervoer van Nederland naar vliegveld Bologna, Italië - Gebruik SPA - Thee, koffie, sappen en alcoholische dranken - Maaltijden en drankjes buiten de locatie [trainer-->]Team Mirthe Vollenga is deskundig op het gebied van dynamische coaching & retraites. Haar passie om spirituele reizen te begeleiden komt, doordat ze van mensen houdt en geboeid blijft door hoe de deelnemers zich ontwikkelen. “In mijn coaching en training ga uit van het principe dat jij meer bent dan je geschiedenis, je oude overtuigingen en patronen. Graag help ik je bij je wezenlijke vragen en het bij het vinden van heldere antwoorden. Ik zet je in beweging op een speelse en intuïtieve manier en laat je jouw wereld van een verschillende kant bekijken en ervaren. Zo kom jij bij jouw basis, je zelfbeeld en je gevoel, waardoor je meer inzicht in jezelf krijgt. Ik zie mijn taak als spiegelend en confronterend, waardoor jij jezelf ontmoet. No nonsens, direct, humor, helder, ontspannen, sprankelend en liefde zijn mijn kernwoorden.”

```html
<!DOCTYPE html>
<html lang="nl">
<head>
<meta charset="utf-8">
<title>Lumenora brochure – voor- en achterzijde</title>
<link rel="stylesheet" href="https://fonts.googleapis.com/css2?family=Open+Sans:wght@400;600;700&display=swap">
<style>
  :root{
    --bg:#e6e4e0;
    --paper:#ffffff;
    --navy:#1f3d6e;
    --navy-deep:#172f57;
    --blue:#1f86c9;
    --green:#7ab33e;
    --orange:#f29a1f;
    --ink:#4a4a4a;
    --muted:#8a8a8a;
    --panel:#eef0f2;
  }
  *{box-sizing:border-box;margin:0;padding:0}
  html,body{width:1200px;height:799px;overflow:hidden}
  body{background:var(--bg);font-family:"Open Sans",Arial,sans-serif;color:var(--ink);position:relative}
  .sheet{position:absolute;top:30px;width:522px;height:739px;background:var(--paper);overflow:hidden;box-shadow:0 2px 8px rgba(0,0,0,.18)}
  .sheet--front{left:46px}
  .sheet--back{left:632px}

  /* front */
  .brand{position:absolute;top:14px;right:22px;display:flex;align-items:center;gap:6px;font-weight:700;font-size:17px;letter-spacing:.5px;color:var(--navy)}
  .brand__dot{width:10px;height:10px;background:var(--green)}
  .hero{position:absolute;top:52px;left:0;width:100%;height:256px;
    background:linear-gradient(180deg,#8fb7df 0%,#c7d9ea 30%,#c9b59a 55%,#9c8466 75%,#6e8a4e 100%)}
  .services{position:absolute;top:308px;left:0;width:100%;height:208px;display:flex}
  .service{flex:1;padding:16px 14px;color:#fff;text-align:center}
  .service--personal{background:var(--green)}
  .service--team{background:var(--blue)}
  .service--org{background:var(--orange)}
  .service__icon{width:30px;height:30px;border-radius:50%;border:2px solid #fff;margin:0 auto 8px}
  .service__title{font-size:14px;font-weight:700;line-height:1.2;margin-bottom:12px}
  .service__text{font-size:9.5px;line-height:1.45}
  .intro{position:absolute;top:530px;left:24px;right:24px}
  .intro__heading{font-size:14.5px;font-weight:700;color:var(--navy);line-height:1.3;margin-bottom:8px}
  .intro p{font-size:8.2px;line-height:1.5;margin-bottom:6px}
  .footer{position:absolute;bottom:0;left:0;width:100%;height:67px;background:var(--navy-deep);color:#fff;
    display:flex;align-items:center;padding:0 22px;gap:26px;font-size:7px;line-height:1.5}
  .footer__brand{margin-left:auto;display:flex;align-items:center;gap:5px;font-size:12px;font-weight:700;letter-spacing:.4px}
  .footer__brand .brand__dot{width:8px;height:8px}

  /* back */
  .titlebar{height:48px;background:var(--navy);color:#fff;font-size:20px;font-weight:600;padding:11px 24px}
  .block{position:absolute;left:24px;right:24px}
  .subtitle{top:58px;font-size:13px;color:var(--blue);font-weight:600}
  .facts{top:82px;font-size:8.5px;line-height:1.55}
  .section-title{font-size:17px;color:var(--navy);font-weight:600;margin-bottom:4px}
  .about{top:128px}
  .body-text{font-size:8.2px;line-height:1.5}
  .strip{position:absolute;top:236px;left:24px;right:24px;height:68px;display:flex;gap:3px}
  .strip__photo{flex:1}
  .strip__photo--a{background:linear-gradient(180deg,#8eb5d8,#b9a27c)}
  .strip__photo--b{background:linear-gradient(180deg,#9fc0de,#7f9a5a)}
  .strip__photo--c{background:linear-gradient(180deg,#a9c6e2,#c2ab84)}
  .trainer{top:320px;display:flex;gap:14px}
  .trainer__photo{flex:none;width:62px;height:62px;border-radius:50%;background:linear-gradient(180deg,#cfd3d6,#a9aeb3)}
  .trainer__name{font-size:16px;color:var(--navy);font-weight:600;margin-bottom:3px}
  .audience{top:410px}
  .price{position:absolute;top:560px;left:24px;right:24px;height:110px;display:flex;background:var(--panel)}
  .price__amount{width:140px;background:var(--green);color:#fff;display:flex;flex-direction:column}
  .price__label{font-size:11px;font-weight:600;padding:6px 12px;background:#68a030}
  .price__value{flex:1;display:flex;align-items:center;padding-left:14px;font-size:26px;font-weight:600}
  .price__list{flex:1;padding:28px 18px 0;display:grid;grid-template-columns:1fr 1fr;gap:8px 14px;font-size:8.5px;list-style:none}
  .price__list li::before{content:"";display:inline-block;width:5px;height:5px;background:var(--green);margin-right:6px;vertical-align:middle}
</style>
</head>
<body>

<section class="sheet sheet--front">
  <div class="brand"><span class="brand__dot"></span>LUMENORA</div>
  <div class="hero" role="img" aria-label="Foto van een Italiaanse heuvelstad met paleistorens onder een blauwe lucht"></div>

  <div class="services">
    <div class="service service--personal">
      <div class="service__icon"></div>
      <h2 class="service__title">Persoonlijke<br>ontwikkeling</h2>
      <p class="service__text">In de Persoonlijke ontwikkeling programma's staat jij centraal met je eigen vragen en doelen.</p>
    </div>
    <div class="service service--team">
      <div class="service__icon"></div>
      <h2 class="service__title">Team<br>ontwikkeling</h2>
      <p class="service__text">In het Team ontwikkeling programma gaan we samen aan de slag met verbinding en heldere afspraken.</p>
    </div>
    <div class="service service--org">
      <div class="service__icon"></div>
      <h2 class="service__title">Organisatie-<br>ontwikkeling</h2>
      <p class="service__text">In de Organisatie-ontwikkeling programma's werken we aan cultuur, leiderschap en duurzame groei van je bedrijf.</p>
    </div>
  </div>

  <div class="intro">
    <h1 class="intro__heading">Het bureau voor Persoonlijke, Team- en Organisatieontwikkeling in Italië.</h1>
    <p>De reis is niet altijd eenvoudig, maar de weg naar jezelf is de moeite waard. Door het juiste proces te doorlopen ontdek je wat je echt drijft en leer je vanuit je kracht te leven.</p>
    <p>Lumenora is de plek waar je opnieuw geboren wordt als mens, als team en als organisatie. In het hart van Italië, tussen de heuvels van Urbino, krijg je de ruimte om te groeien.</p>
    <p>Wij werken met ervaren professionals uit Nederland en Italië die jou met passie en deskundigheid begeleiden op je pad naar meer inzicht en vrijheid.</p>
  </div>

  <footer class="footer">
    <div>Lumenora Coaching B.V.<br>Postbus 218, 3500 AE Utrecht<br>Tel. +31 (0)30 555 0192</div>
    <div>info@lumenora-coaching.nl<br>www.lumenora-coaching.nl</div>
    <div class="footer__brand"><span class="brand__dot"></span>LUMENORA</div>
  </footer>
</section>

<section class="sheet sheet--back">
  <div class="titlebar">Your Title here</div>
  <p class="block subtitle">Place your subtitle here.</p>
  <p class="block facts">Location: Via dei Tigli 14, 61029 Urbino (PU), Italia<br>Duration: 5 days<br>Dates: March 1, 2015 – March 5, 2015</p>

  <div class="block about">
    <h2 class="section-title">About the program:</h2>
    <p class="body-text">Lorem ipsum dolor sit amet, consectetur adipiscing elit, sed do eiusmod tempor incididunt ut labore et dolore magna aliqua. Ut enim ad minim veniam, quis nostrud exercitation ullamco laboris nisi ut aliquip ex ea commodo consequat. Duis aute irure dolor in reprehenderit in voluptate velit esse cillum dolore eu fugiat nulla pariatur.</p>
  </div>

  <div class="strip">
    <div class="strip__photo strip__photo--a" role="img" aria-label="Foto van een stadsgezicht met torens"></div>
    <div class="strip__photo strip__photo--b" role="img" aria-label="Foto van een glooiend heuvellandschap"></div>
    <div class="strip__photo strip__photo--c" role="img" aria-label="Foto van een plein met historische gevels"></div>
  </div>

  <div class="block trainer">
    <div class="trainer__photo" role="img" aria-label="Portretfoto van de trainer"></div>
    <div>
      <h2 class="trainer__name">Trainer's Name</h2>
      <p class="body-text">Lorem ipsum dolor sit amet, consectetur adipiscing elit, sed do eiusmod tempor incididunt ut labore et dolore magna aliqua. Ut enim ad minim veniam, quis nostrud exercitation ullamco laboris nisi ut aliquip ex ea commodo.</p>
    </div>
  </div>

  <div class="block audience">
    <h2 class="section-title">Who is this for?</h2>
    <p class="body-text">Lorem ipsum dolor sit amet, consectetur adipiscing elit, sed do eiusmod tempor incididunt ut labore et dolore magna aliqua. Ut enim ad minim veniam, quis nostrud exercitation ullamco laboris nisi ut aliquip ex ea commodo consequat. Duis aute irure dolor in reprehenderit in voluptate velit esse cillum.</p>
  </div>

  <div class="price">
    <div class="price__amount">
      <span class="price__label">Price includes:</span>
      <span class="price__value">$1000</span>
    </div>
    <ul class="price__list">
      <li>Lorem ipsum dolor sit amet</li>
      <li>Lorem ipsum dolor sit amet</li>
      <li>Lorem ipsum dolor sit amet</li>
      <li>Lorem ipsum dolor sit amet</li>
    </ul>
  </div>
</section>

</body>
</html>
```